elegant beautiful Hang tag for a novelty makeup towel

It's a black hand towel in the shape of a little black dress. it is called VELVET EVENING CLOTH, it is a CLEAN SLATE FACE CLOTH. (doesn't show our makeup stains) Made in USA

Target Market(s)

ALL Women , Makeup artists, novelty THIS WILL BE IN THE HALVERDALE STORES AND PRESCOTWICK STORES.

Industry/Entity Type

Makeup

Contact Information for Business Card

I actually need a hang tag for a homemade handmade towel. I have a logo that I want on the tag and know what we want to say on it, on back needs to say "The essential to every girl's wardrobe. So when the little black dress comes off, our VELVET EVENING CLOTH is there to help you wash your day away. Include website www.velveteveningcloth.example OH INCLUDE TM (trademark sign next to logo please. Also, in small print on back from the makers of THE ORIGINAL CLEAN SLATE FACE CLOTH. handmade in USA. also CLEAN SLATE FACE CLOTH IN big font on front under logo sign with light colored pink lips after 'NO SHOW" but have no idea about fonts, graphics, placement or design. Want it classy, elegant, girly! COLORS LIGHT BEIGER BACKGROUND WITH BLACK WRITING/ DESIGNS

Font styles to use
Serif
Decorative
Script

Colors
fff3d1

Requirements
Must have
• Black cream girly , also state in big writing that it's a " clean slate face cloth" with a tiny light pink lip between the show and makeup. Include www.velveteveningcloth.example Quillfern Goods, LLC
Nice to have
• Perhaps an outline of a little black dress. A black scroll edge of some sort around card. Classy

```html
<!DOCTYPE html>
<html lang="en">
<head>
<meta charset="utf-8">
<title>Velvet Evening Cloth – Hang Tag</title>
<link rel="stylesheet" href="https://fonts.googleapis.com/css2?family=Archivo+Black&family=Exo+2:wght@300;400&display=swap">
<style>
  :root {
    --cream: #fff3d1;
    --ink: #1f1b1c;
    --logo-ink: #322a2a;
    --paper: #ffffff;
    --label-dark: #b2a892;
    --label-light: #ddd0b2;
    --lip-pink: #f4b8c4;
  }
  html, body {
    margin: 0;
    padding: 0;
    background: var(--paper);
    overflow: hidden;
  }
  .sheet {
    position: relative;
    width: 934px;
    height: 1200px;
    overflow: hidden;
    background: var(--paper);
  }
  .tag-side {
    position: absolute;
    left: 0;
    width: 934px;
    height: 584px;
    display: block;
  }
  .tag-side--front { top: 0; }
  .tag-side--back { top: 616px; }
  .panel { fill: var(--cream); }
  .title-wedge { fill: var(--ink); stroke: #3a3435; stroke-width: 1; }
  .product-title {
    font-family: "Exo 2", sans-serif;
    font-weight: 300;
    font-size: 47px;
    fill: var(--cream);
  }
  .lips { fill: var(--lip-pink); }
  .logo-frame { fill: none; stroke: var(--logo-ink); stroke-width: 15; stroke-linejoin: miter; }
  .logo-frame--back { stroke: var(--ink); }
  .brand-name {
    font-family: Arial, "Helvetica Neue", sans-serif;
    font-weight: 400;
    fill: var(--ink);
  }
  .origin-label {
    font-family: "Archivo Black", sans-serif;
    font-size: 34px;
    fill: url(#label-fade);
  }
  .tagline {
    font-family: "Exo 2", sans-serif;
    font-weight: 400;
    font-size: 34px;
    fill: var(--ink);
  }
  .story {
    font-family: "Exo 2", sans-serif;
    font-weight: 300;
    font-size: 22px;
    fill: var(--ink);
  }
  .web-address {
    font-family: "Exo 2", sans-serif;
    font-weight: 400;
    font-size: 29px;
    fill: var(--ink);
  }
  .maker-band { fill: var(--ink); }
  .maker-item {
    font-family: "Exo 2", sans-serif;
    font-weight: 400;
    font-size: 17px;
    fill: var(--cream);
  }
</style>
</head>
<body>
<main class="sheet">

  <svg class="tag-side tag-side--front" viewBox="0 0 934 584" aria-label="Hang tag front">
    <defs>
      <linearGradient id="label-fade" x1="0" x2="1" y1="0" y2="0">
        <stop offset="0" stop-color="var(--label-dark)"/>
        <stop offset="1" stop-color="var(--label-light)"/>
      </linearGradient>
    </defs>
    <rect class="panel" x="0" y="0" width="934" height="584"/>
    <polygon class="title-wedge" points="19,24 913,24 913,528"/>
    <text class="product-title" x="890" y="86" text-anchor="end">CLEAN SLATE</text>
    <ellipse class="lips" cx="618" cy="124" rx="22" ry="10" role="img" aria-label="Light pink lips"/>
    <text class="product-title" x="890" y="142" text-anchor="end">FACE CLOTH</text>

    <polygon class="logo-frame" points="115,318 202,368 202,470 115,520 28,470 28,368"/>
    <text class="brand-name" x="115" y="402" font-size="26" text-anchor="middle">VELVET</text>
    <text class="brand-name" x="115" y="432" font-size="26" text-anchor="middle">EVENING</text>
    <text class="brand-name" x="115" y="462" font-size="26" text-anchor="middle">CLOTH<tspan font-size="12" dy="-12">TM</tspan></text>

    <text class="origin-label" x="532" y="503">MADE IN USA</text>
    <text class="web-address" x="467" y="569" text-anchor="middle">www.velveteveningcloth.example</text>
  </svg>

  <svg class="tag-side tag-side--back" viewBox="0 0 934 584" aria-label="Hang tag back">
    <rect class="panel" x="0" y="0" width="934" height="584"/>
    <text class="tagline" x="467" y="80" text-anchor="middle">The essential to every girl's wardrobe.</text>

    <polygon class="logo-frame logo-frame--back" points="467,130 562,185 562,295 467,350 372,295 372,185"/>
    <text class="brand-name" x="467" y="218" font-size="30" text-anchor="middle">VELVET</text>
    <text class="brand-name" x="467" y="252" font-size="30" text-anchor="middle">EVENING</text>
    <text class="brand-name" x="467" y="286" font-size="30" text-anchor="middle">CLOTH<tspan font-size="13" dy="-14">TM</tspan></text>

    <text class="story" x="467" y="398" text-anchor="middle">So when the little black dress comes off, our</text>
    <text class="story" x="467" y="428" text-anchor="middle">VELVET EVENING CLOTH is there to help you wash your day away.</text>

    <rect class="maker-band" x="0" y="485" width="934" height="45"/>
    <text class="maker-item" x="30" y="514">Handmade in USA</text>
    <text class="maker-item" x="467" y="514" text-anchor="middle">From the makers of THE ORIGINAL CLEAN SLATE FACE CLOTH</text>
    <text class="maker-item" x="900" y="514" text-anchor="end">Quillfern Goods, LLC</text>

    <text class="web-address" x="467" y="569" text-anchor="middle">www.velveteveningcloth.example</text>
  </svg>

</main>
</body>
</html>
```